Wedding invitation

Hello,

I would like the same attached image in a vertical rectangular 3D effect design, same colours,
but without text.

I would like eaxctly like the attachment design, in a long vertical, ration 16:9 size for social media.

```html
<!DOCTYPE html>
<html lang="en">
<head>
<meta charset="UTF-8">
<title>Wedding Invitation – Front and Back</title>
<link rel="stylesheet" href="https://fonts.googleapis.com/css2?family=Pinyon+Script&family=Cormorant+Garamond:wght@500&display=swap">
<style>
  :root {
    --backdrop: #8f939a;
    --card-edge: #1c2130;
    --card-mid: #2a3040;
    --panel-light: #545b68;
    --panel-dark: #262c3a;
    --emboss-light: rgba(120, 130, 150, 0.35);
    --emboss-dark: rgba(5, 8, 15, 0.55);
    --gold: #c99a5c;
    --gold-light: #e7c48d;
    --ink: #f4f1ea;
  }
  * { margin: 0; padding: 0; box-sizing: border-box; }
  html, body { width: 1200px; height: 960px; overflow: hidden; }
  body {
    background: var(--backdrop);
    position: relative;
    font-family: "Cormorant Garamond", "Times New Roman", serif;
    color: var(--ink);
  }
  .card {
    position: absolute;
    top: 50px;
    width: 485px;
    height: 860px;
    background: linear-gradient(160deg, var(--card-mid), var(--card-edge));
    overflow: hidden;
  }
  .card--front { left: 100px; }
  .card--back { left: 616px; }

  .emboss {
    position: absolute;
    border: 1px solid var(--emboss-dark);
    box-shadow: inset 1px 1px 0 var(--emboss-light), 1px 1px 0 var(--emboss-light);
  }
  .emboss--outer { inset: 18px 16px; }
  .emboss--mid { inset: 24px 22px; }
  .emboss--inner { inset: 30px 28px; }

  .panel {
    position: absolute;
    left: 54px; top: 46px; width: 377px; height: 768px;
    background: radial-gradient(ellipse 70% 55% at 50% 35%, var(--panel-light), var(--panel-dark) 100%);
  }
  .gold-frame {
    position: absolute;
    border: 2px solid var(--gold);
    box-shadow: 0 0 0 0.5px var(--gold-light) inset;
  }
  .gold-frame--tall { left: 70px; top: 46px; width: 344px; height: 768px; }
  .gold-frame--wide { left: 54px; top: 62px; width: 377px; height: 736px; }

  .line {
    position: absolute;
    left: 0; width: 100%;
    text-align: center;
    text-transform: uppercase;
    font-size: 14px;
    letter-spacing: 0.2px;
    line-height: 18px;
  }
  .invite-lead { top: 114px; }
  .couple-name {
    position: absolute;
    left: 0; width: 100%;
    text-align: center;
    font-family: "Pinyon Script", cursive;
    font-size: 62px;
    line-height: 1;
  }
  .couple-name--first { top: 250px; }
  .couple-name--second { top: 410px; }
  .divider {
    position: absolute;
    top: 321px; left: 130px; width: 225px; height: 16px;
    display: flex; align-items: center; justify-content: space-between;
    font-size: 14px; text-transform: uppercase;
  }
  .divider::before, .divider::after {
    content: ""; width: 83px; height: 1px; background: var(--ink);
  }
  .event-date {
    position: absolute;
    top: 480px; left: 0; width: 100%;
    display: flex; justify-content: center; align-items: center; gap: 26px;
    font-size: 12px;
  }
  .event-date__day {
    font-family: "Pinyon Script", cursive;
    font-size: 48px; line-height: 48px;
  }
  .ceremony-time { top: 574px; font-size: 13px; }
  .venue-address { top: 610px; font-size: 13px; }
  .reception-note {
    position: absolute; top: 690px; left: 0; width: 100%;
    text-align: center;
    font-family: "Pinyon Script", cursive;
    font-size: 38px;
  }
</style>
</head>
<body>
  <section class="card card--front" aria-label="Invitation front">
    <div class="emboss emboss--outer"></div>
    <div class="emboss emboss--mid"></div>
    <div class="emboss emboss--inner"></div>
    <div class="panel"></div>
    <div class="gold-frame gold-frame--tall"></div>
    <div class="gold-frame gold-frame--wide"></div>

    <p class="line invite-lead">You are invited to<br>the wedding of</p>
    <h1 class="couple-name couple-name--first">Name Here</h1>
    <div class="divider">and</div>
    <h1 class="couple-name couple-name--second">Name Here</h1>
    <p class="event-date"><span>SEPT</span><span class="event-date__day">24</span><span>2025</span></p>
    <p class="line ceremony-time">Ceremony to commence at xx:xxpm</p>
    <p class="line venue-address">Address line 01 goes here<br>Address line 2 goes here</p>
    <p class="reception-note">Reception to follow</p>
  </section>

  <section class="card card--back" aria-label="Invitation back">
    <div class="emboss emboss--outer"></div>
    <div class="emboss emboss--mid"></div>
    <div class="emboss emboss--inner"></div>
    <div class="panel"></div>
    <div class="gold-frame gold-frame--tall"></div>
    <div class="gold-frame gold-frame--wide"></div>
  </section>
</body>
</html>
```